Online retailer needs a Quirky yet professionally designed double sided business car

We mainly sell kitchen and home accessories but pretty much anything new and in demand. Have a look at our site and then come up with designs.
Design to be really catching and want people to visit the website.
Final details such as number, director name and email address will be given to the designer of the winning business card.

Www.zapvelbo.com

Ideas out of the norm also welcome!!

Industry/Entity Type

Business

```html
<!DOCTYPE html>
<html lang="en">
<head>
<meta charset="utf-8">
<title>Zapvelbo – Business Card</title>
<link rel="stylesheet" href="https://fonts.googleapis.com/css2?family=Questrial&family=Poppins:wght@700&display=swap">
<style>
  :root {
    --canvas: #e9e6e1;
    --orange-light: #f7941d;
    --orange-deep: #f15a24;
    --orange-shade: #e2541f;
    --panel: #fbb040;
    --ink: #231f20;
    --white: #ffffff;
  }
  * { margin: 0; padding: 0; box-sizing: border-box; }
  html, body { width: 1200px; height: 914px; overflow: hidden; }
  body {
    background: var(--canvas);
    font-family: "Questrial", sans-serif;
    position: relative;
  }
  .card {
    position: absolute;
    left: 280px;
    width: 640px;
    height: 366px;
    overflow: hidden;
    background: linear-gradient(135deg, var(--orange-light) 0%, var(--orange-deep) 100%);
    box-shadow: 0 6px 18px rgba(0,0,0,0.18);
  }
  .card--back { top: 50px; }
  .card--front { top: 486px; }
  .card svg.card__shapes { position: absolute; inset: 0; }

  /* back side */
  .name-tag__label {
    position: absolute;
    left: 78px; top: 78px;
    font-family: "Poppins", sans-serif;
    font-weight: 700;
    font-size: 28px;
    color: var(--ink);
  }
  .contact-list {
    position: absolute;
    left: 300px; top: 110px;
    list-style: none;
  }
  .contact-list__item {
    display: flex;
    align-items: center;
    gap: 14px;
    height: 40px;
    color: var(--white);
    font-size: 21px;
  }
  .contact-list__icon { width: 20px; height: 20px; flex: none; }

  /* front side */
  .brand {
    position: absolute;
    left: 40px; top: 92px;
    width: 560px;
    text-align: center;
  }
  .brand__name {
    font-size: 86px;
    line-height: 1;
    color: var(--ink);
  }
  .brand__tagline {
    margin-top: 10px;
    font-size: 24px;
    color: var(--orange-deep);
  }
  .front-url {
    position: absolute;
    left: 110px; top: 300px;
    font-size: 28px;
    color: var(--white);
  }
</style>
</head>
<body>

<section class="card card--back" aria-label="Business card, contact side">
  <svg class="card__shapes" width="640" height="366" viewBox="0 0 640 366">
    <polygon class="name-tag__band" points="30,0 60,0 60,190 30,205" fill="var(--orange-deep)"/>
    <rect class="name-tag__panel" x="60" y="0" width="200" height="190" fill="var(--panel)"/>
    <polygon class="name-tag__fold" points="228,190 260,190 260,160" fill="var(--white)"/>
  </svg>
  <div class="name-tag__label">Your Name</div>

  <ul class="contact-list">
    <li class="contact-list__item">
      <svg class="contact-list__icon" viewBox="0 0 20 20"><path d="M10 1a6 6 0 0 0-6 6c0 5 6 12 6 12s6-7 6-12a6 6 0 0 0-6-6zm0 8.5a2.5 2.5 0 1 1 0-5 2.5 2.5 0 0 1 0 5z" fill="var(--white)"/></svg>
      Type Address here, Address
    </li>
    <li class="contact-list__item">
      <svg class="contact-list__icon" viewBox="0 0 20 20"><rect x="5" y="1" width="10" height="18" rx="2" fill="var(--white)"/><rect x="7" y="4" width="6" height="10" fill="var(--orange-light)"/></svg>
      0123 456 789
    </li>
    <li class="contact-list__item">
      <svg class="contact-list__icon" viewBox="0 0 20 20"><rect x="1" y="4" width="18" height="12" fill="var(--white)"/><path d="M1 4l9 7 9-7" fill="none" stroke="var(--orange-light)" stroke-width="1.6"/></svg>
      xyz_zv@123.com
    </li>
    <li class="contact-list__item">
      <svg class="contact-list__icon" viewBox="0 0 20 20"><circle cx="10" cy="10" r="8.5" fill="none" stroke="var(--white)" stroke-width="2"/><ellipse cx="10" cy="10" rx="3.5" ry="8.5" fill="none" stroke="var(--white)" stroke-width="1.6"/><path d="M2 10h16" stroke="var(--white)" stroke-width="1.6"/></svg>
      www.zapvelbo.com
    </li>
  </ul>
</section>

<section class="card card--front" aria-label="Business card, brand side">
  <svg class="card__shapes" width="640" height="366" viewBox="0 0 640 366">
    <polygon class="speech-panel__shadow" points="0,250 600,250 640,290 640,366 0,366" fill="var(--orange-shade)"/>
    <rect class="speech-panel" x="40" y="60" width="560" height="190" fill="var(--panel)"/>
    <polygon class="speech-panel__tail" points="60,249 110,249 70,300" fill="var(--panel)"/>
  </svg>
  <div class="brand">
    <div class="brand__name">Zapvelbo</div>
    <div class="brand__tagline">brighten your kitchen</div>
  </div>
  <div class="front-url">www.zapvelbo.com</div>
</section>

</body>
</html>
```